Zielgruppe
Hausarztpraxis Dr. Wildhagen
Patientenbetreuung / Junge Patienten
Aufgabenstellung
Bitte Mit dem Praxis Logo. Gern auch ein Foto aus der Praxis. In den Farben der Praxis Weiß-Magenta-Grau
Es soll kein Newsletter an sich werden, sondern eine Email die die Patienten nach Ihrem Besuch in der Praxis bekommen. Dort soll dann die Suchflixseite verlinkt sein mit einem Button zum bewerten!

```html
<!DOCTYPE html>
<html lang="de">
<head>
<meta charset="utf-8">
<title>Bewertungs-E-Mail – Hausarztpraxis Dr. Wildhagen</title>
<link rel="stylesheet" href="https://fonts.googleapis.com/css2?family=Open+Sans:wght@400;600;700&display=swap">
<style>
  :root {
    --magenta: #c21a55;
    --magenta-soft: rgba(196, 28, 88, 0.82);
    --pink-band: #ee6a9c;
    --text-grey: #5a5a5a;
    --white: #ffffff;
    --star: #f5b800;
    --photo-light: #eeecea;
    --photo-dark: #cfcbc6;
  }
  * { margin: 0; padding: 0; box-sizing: border-box; }
  html, body { width: 1137px; height: 1200px; overflow: hidden; background: var(--white); }
  body { position: relative; font-family: "Open Sans", sans-serif; color: var(--text-grey); }

  .practice-mark { position: absolute; top: 24px; left: 0; width: 1137px; text-align: center; }
  .practice-mark__dot { width: 60px; height: 60px; border-radius: 50%; border: 3px solid var(--magenta); margin: 0 auto 14px; }
  .practice-mark__name { font-size: 19px; font-weight: 600; color: var(--magenta); letter-spacing: 0.5px; }

  .hero-photo {
    position: absolute; top: 173px; left: 0; width: 1137px; height: 318px;
    background: linear-gradient(90deg, var(--photo-light) 0%, var(--photo-dark) 100%);
  }

  .hero-box {
    position: absolute; top: 408px; left: 246px; width: 645px; height: 143px;
    background: var(--magenta-soft); color: var(--white); text-align: center;
  }
  .hero-box__title { font-size: 33px; font-weight: 400; margin-top: 34px; line-height: 1.2; }
  .hero-box__lead { font-size: 14.5px; margin-top: 10px; }

  .message { position: absolute; top: 607px; left: 242px; width: 653px; text-align: center; font-size: 13.5px; line-height: 19px; }
  .message p { margin-bottom: 19px; }

  .review-button {
    display: block; width: 645px; height: 39px; border-radius: 20px; background: var(--magenta);
    color: var(--white); font-size: 12.5px; line-height: 39px; text-decoration: underline; margin: 29px 0 27px 4px;
  }
  .phone { color: var(--magenta); font-weight: 700; }

  .review-badge { position: absolute; top: 1058px; left: 478px; display: flex; align-items: flex-start; gap: 8px; }
  .review-badge__dot { width: 40px; height: 40px; border-radius: 50%; background: #4a7fe0; margin-top: 2px; }
  .review-badge__text { font-size: 13px; font-weight: 600; color: #555; line-height: 16px; }
  .review-badge__stars { display: flex; gap: 3px; margin-top: 4px; }

  .footer-band { position: absolute; top: 1160px; left: 0; width: 1137px; height: 11px; background: var(--pink-band); }
  .footer { position: absolute; top: 1171px; left: 0; width: 1137px; height: 29px; background: var(--magenta);
    color: var(--white); text-align: center; font-size: 13px; line-height: 29px; }
</style>
</head>
<body>
  <header class="practice-mark">
    <div class="practice-mark__dot"></div>
    <div class="practice-mark__name">Hausarztpraxis Dr. Wildhagen</div>
  </header>

  <div class="hero-photo" role="img" aria-label="Foto des hellen Wartebereichs der Praxis"></div>

  <section class="hero-box">
    <h1 class="hero-box__title">Ihre Meinung ist uns wichtig.</h1>
    <p class="hero-box__lead">Nehmen Sie sich kurz zeit und bewerten Sie uns auf Suchflix.</p>
  </section>

  <main class="message">
    <p>Hallo Frau/Herr....,</p>
    <p>wie war Ihre Erfahrung bei Dr. Med. Henrike Wildhagen?</p>
    <p>Wir versuchen ständig, uns zu verbessern und freuen uns, wenn du uns dein Feedback mitteilen könntest. Es wäre toll, wenn du dir kurz die Zeit nimmst, eine Bewertung bei Suchflix zu schreiben, denn damit hilfst du uns und auch anderen Kunden uns zu finden.</p>
    <p>Um Ihre Bewertung zu schreiben und abzuschicken, genügt ein Klick!</p>
    <a class="review-button" href="#">Jetzt Hausarztpraxis Dr.Med.Henrike Wildhagen bewerten</a>
    <p>Vielen Dank im Voraus für deine Bewertung! Bei Fragen oder falls Sie uns erneut besuchen möchtest, stehen wir dir jederzeit gerne zur Verfügung!</p>
    <p>Rufen Sie uns an unter der <span class="phone">01234- 56 78</span>.</p>
    <p>Viele Grüße,<br>Ihre Hausarztpraxis</p>
  </main>

  <div class="review-badge">
    <div class="review-badge__dot"></div>
    <div>
      <div class="review-badge__text">Bewerten Sie uns<br>auf suchflix!</div>
      <div class="review-badge__stars">
        <svg width="92" height="16" viewBox="0 0 92 16" aria-hidden="true">
          <defs><polygon id="star" points="8,0 10,5.6 16,6 11.3,9.7 13,15.5 8,12.2 3,15.5 4.7,9.7 0,6 6,5.6"/></defs>
          <use href="#star" x="0" fill="var(--star)"/>
          <use href="#star" x="19" fill="var(--star)"/>
          <use href="#star" x="38" fill="var(--star)"/>
          <use href="#star" x="57" fill="var(--star)"/>
          <use href="#star" x="76" fill="var(--star)"/>
        </svg>
      </div>
    </div>
  </div>

  <div class="footer-band"></div>
  <footer class="footer">Impressum &nbsp;I Datenschutz I Unsere Praxis I Kontakt</footer>
</body>
</html>
```